New Book Cover Design Project for The Lantern Keeper

I need a book cover designed for my book, "Seven Quiet Paths to a Bigger Income, Leave the Office Behind, and Build the Life You Picture!" The cover needs to include my logo. It's a step by step guide to earning money from home in various different ways. By doing this, people can quit their jobs and live their dream life. A life with purpose, happiness and abundance. I would love an image of a lady in a suit crushing a desk, or of someone sitting on a island or of money abundantly flowing or a combination of all of these things. It needs to represent the dream life and be visually strong to look at. It needs to include the logo at the top. Its important that people identify with it instantly.
Updates

Project Deadline Extended Reason: I've extended the deadline as I realised I not provided some key details such as dimensions of the book, author's name plus details for the back cover. Thanks. Added Sunday, August 6, 2017

Target Market(s)

Women over 30 who are fed up with working in a cubicle and of corporate life.

Industry/Entity Type

Entrepreneur

Font styles to use
Other font styles liked:
• Arial Narrow or Century Gothic or something fun!

Colors

Designer to choose colors to be used in the design.

Requirements
Must have
• My logo at the top (non-negotiable). It needs to convey someone living their dreams or quitting their job or crushing their cubicle. I want it to be like no other title. Visually strong, clear and representative of what it is about. This book represents an opportunity for people to transform their lives! I want them to see this book and want to buy it.
Nice to have
• Examples could be leaving their desk and entering through a door to an amazing life. Money could feature somewhere in it. It needs to represent the dream and someone attaining it. It could feature balloons to escape their desk, or climbing out of their desk to an amazing life.
Should not have
• Anything scary! I don't want too many images or confusing images.

```html
<!DOCTYPE html>
<html lang="en">
<head>
<meta charset="utf-8">
<title>Back Cover – The Lantern Keeper</title>
<link rel="stylesheet" href="https://fonts.googleapis.com/css2?family=Arimo:wght@700&family=Open+Sans:ital,wght@0,400;0,700;1,400;1,700&display=swap">
<style>
  :root {
    --paper: #ffffff;
    --ink: #111111;
    --frame: #222222;
    --office-shadow: #6e6a63;
    --office-mid: #b9b6ae;
    --office-light: #e6e4df;
    --fabric: #cfcdc8;
    --fabric-light: #dad8d3;
    --portrait-top: #3b3f48;
    --portrait-mid: #5d6370;
    --portrait-low: #8fa6d6;
  }
  * { box-sizing: border-box; margin: 0; padding: 0; }
  html, body { width: 815px; height: 1200px; overflow: hidden; background: var(--paper); }
  .back-cover {
    position: relative;
    width: 815px;
    height: 1200px;
    background: var(--paper);
    border: 1px solid var(--frame);
    font-family: "Open Sans", Arial, sans-serif;
    color: var(--ink);
  }
  .hero-scene {
    position: absolute;
    left: 46px; top: 46px;
    width: 722px; height: 416px;
    background:
      linear-gradient(90deg,
        var(--office-mid) 0%, var(--office-light) 12%, var(--office-shadow) 26%,
        var(--office-mid) 38%, var(--office-light) 39.5%,
        var(--fabric-light) 41%, var(--fabric) 75%, var(--fabric-light) 100%);
  }
  .hero-headline {
    position: absolute;
    left: 282px; top: 149px;
    width: 400px;
    text-align: center;
    font-family: "Arimo", Arial, sans-serif;
    font-weight: 700;
    font-size: 22.5px;
    line-height: 28px;
    color: var(--ink);
  }
  .pitch {
    position: absolute;
    left: 10px; right: 10px; top: 461px;
    text-align: center;
    font-style: italic;
    font-size: 17px;
    line-height: 26.7px;
  }
  .callout {
    position: absolute;
    left: 10px; right: 10px; top: 781px;
    text-align: center;
    font-weight: 700;
    font-size: 15.8px;
    line-height: 26.7px;
  }
  .experts-intro {
    position: absolute;
    left: 10px; right: 10px; top: 834px;
    text-align: center;
    font-size: 15.8px;
    line-height: 26.7px;
  }
  .experts-list {
    position: absolute;
    left: 20px; right: 20px; top: 864px;
    text-align: center;
    font-size: 11.8px;
    line-height: 27px;
  }
  .rally {
    position: absolute;
    left: 10px; right: 10px; top: 916px;
    text-align: center;
    font-weight: 700;
    font-size: 15.8px;
    line-height: 26.7px;
  }
  .author-bio {
    position: absolute;
    left: 46px; top: 976px;
    width: 556px;
    font-style: italic;
    font-size: 17px;
    line-height: 28.3px;
  }
  .author-bio strong { font-weight: 700; }
  .author-portrait {
    position: absolute;
    left: 609px; top: 915px;
    width: 157px; height: 235px;
    border: 1px solid #555;
    background: linear-gradient(180deg, var(--portrait-top) 0%, var(--portrait-mid) 50%, var(--portrait-low) 100%);
  }
</style>
</head>
<body>
  <main class="back-cover">
    <div class="hero-scene" role="img" aria-label="Photo of an office worker peeking around a grey fabric cubicle wall in an office corridor">
      <h2 class="hero-headline">ARE YOU READY TO BECOME<br>A LANTERN KEEPER?</h2>
    </div>

    <p class="pitch">
      Are you searching for a better way to live? If you're tired of working for someone else's dreams<br>
      and want to start working on yours, then this book will help you<br>
      create a life free from the cubicle.<br>
      Imagine the freedom from the 9 to 5!<br>
      Imagine earning 6 figures from home! What would that do for you and your family?<br>
      What would life be like?<br>
      Imagine being able to choose your own hours!<br>
      Imagine being able to work when and where you want!<br>
      Imagine being able to take your children to school and pick them up!<br>
      There are hundreds of ways to earn an income from your computer now that will allow you to<br>
      crush your cubicle-dwelling job. In this book, you'll find the stories and strategies of some<br>
      successful lantern keepers! So let's get crushing!
    </p>

    <p class="callout">
      LEARN FROM AN AMAZING LIST OF EXPERTS ON HOW YOU CAN EARN 6 FIGURES FROM<br>
      HOME AND CRUSH THE CUBICLE!
    </p>

    <p class="experts-intro">Your list of experts includes:</p>

    <p class="experts-list">
      Rosalind Ashby, Derek Lau, Tessa Whitlow, Nora Penhale, Ilona Marsh, Celia Dunmore, Livia Orsan, Warren Tse,<br>
      Serena Valenti, Marcus Hale, Brielle Carter, Helena Forsyth, Josie Radnor and Lucia Benton.
    </p>

    <p class="rally">LET'S GET CRUSHING!</p>

    <p class="author-bio">
      <strong>Maren Holloway</strong> is The Lantern Keeper who has devoted herself to<br>
      understanding how to build a life beyond the cubicle. She is passionate<br>
      about helping others to live a life with purpose and achieve the life of<br>
      their dreams
    </p>

    <div class="author-portrait" role="img" aria-label="Author portrait: smiling woman with dark curly hair in a blue patterned top"></div>
  </main>
</body>
</html>
```